Web design for our new company

We need a web design for our product and for our company.
And the main is our Product tool called "veltor".
----------------------------------------------------------
[Our company's Goal]
Make organization’s communication smooth and healthy with transparency and efficiency for works and tasks in all levels with our workflow tool.

[Our Mission]
Our mission is to achieve business goals with customers.
We work together to identify the goals for your company, guides your strategy and bring the technology answers which best fit to achieve the goals.

[What we do]
We have a workflow tool "veltor"
- Very simple end-user configurable workflow for any company processes
(Targeting small-med size company)
- Graphical & fun features for startup users
- Simple and easy task control with mailbox e-mail look & feel
- Non charged skill up guidance
- Additional features with;
Multiple delegation
Clear status for each owner
Task owner management console with due date reminders&reporting

Others
1. System Development & Implementation Service
Our client list includes a wide variety of small to medium to major sized enterprises.
We can offer from full-scratch based development to packaged system implementation.

2. Project Management(PM) Service
We will provide end-to-end PM service with experienced PM.
Our service is not only “managing” but “leading” to bring success to achieve the goal.

3.Consultation Service

Consulting services to a wide range of fields such as creating business strategy, business process Kaizen, IT system consultation and change management.

Target Market(s)

Business to Business
Mainly to medium size - startup company

Industry/Entity Type

It Company

Coding

Coded - Design and coding required

Number of Pages Required

5+ page

Colors
0255a3
33a6d7
86cfc6
33b8a4
add136
cadf82
fbf289
fee18a
faa54b

Requirements
Must have
• We need Pages for
• Company mission
• Service Overview
• Contact
• Privacy Policy
• Terms and Conditions
• =========================
• As there were some questions, I add followings.---------
• 1. File Format
• We are going to use Amazon web services to upload finished web files.
• The finished files should be ready to use by simply replacing images and text.
• Please provide me "easy to handle" template with "sophisticated design".
• Thanks!
• 2. Multiple Languages
• We need buttons for changing language.
• We will have this translated to German, English and Japanese.
• Thank you so much!!
Nice to have
• These are current Logos and will be a next project to revise them...
• Attached Company Profile and Logo design
• 1. Company Profile
• 2. Our Company Logo
• 3. Our Product Logo -> This is most close to our image of design base.
• 4. Product Logo for PPT Header
• All just for your reference.
• ---------
• As there were some request, I added attachment as for contents for Our mission page.
Should not have
• I hope to see some unique designs.
• (Sorry please ignore my last update as I checked with our CEO.
• Bootstrap is absolutely good template.)

```html
<!DOCTYPE html>
<html lang="en">
<head>
<meta charset="utf-8">
<title>veltor – Workflow Tool</title>
<link rel="stylesheet" href="https://fonts.googleapis.com/css2?family=Open+Sans:wght@400;600;700&display=swap">
<style>
  :root {
    --blue: #0f66b8;
    --blue-deep: #0255a3;
    --orange: #faa54b;
    --teal: #33b8a4;
    --lime: #add136;
    --ink: #2b2b2b;
    --grey-bg: #f2f2f2;
    --white: #ffffff;
  }
  * { box-sizing: border-box; margin: 0; padding: 0; }
  html, body { width: 1200px; height: 3020px; overflow: hidden; }
  body { font-family: "Open Sans", Arial, sans-serif; color: var(--ink); background: var(--white); position: relative; }

  .site-header { position: absolute; top: 0; left: 0; width: 1200px; height: 151px; background: var(--white); }
  .lang-switch { position: absolute; left: 1023px; top: 16px; width: 153px; height: 36px; border: 2px solid #555; border-radius: 18px; display: flex; align-items: center; gap: 8px; padding-left: 16px; font-size: 14px; color: #333; }
  .lang-switch .flag { width: 30px; height: 18px; background: linear-gradient(#b22234 0 50%, #f5f5f5 50% 100%); border-radius: 2px; }
  .brand-name { position: absolute; left: 22px; top: 62px; font-size: 54px; font-weight: 600; color: var(--ink); line-height: 1; }
  .main-nav { position: absolute; top: 96px; left: 620px; font-size: 27px; font-weight: 600; color: var(--blue-deep); letter-spacing: 1px; }
  .main-nav a { color: inherit; text-decoration: none; position: absolute; white-space: nowrap; }
  .main-nav a.active { color: var(--orange); }

  .hero { position: absolute; top: 151px; left: 0; width: 1200px; height: 624px;
    background: linear-gradient(160deg, #3a4350 0%, #6c7684 35%, #2c3440 70%, #11151c 100%);
    clip-path: polygon(0 0, 100% 0, 100% 100%, 50% 80%, 0 98%); }
  .welcome-card { position: absolute; left: 270px; top: 439px; width: 660px; height: 441px; background: var(--white); box-shadow: 0 4px 10px rgba(0,0,0,.2); text-align: center; }
  .section-title { font-size: 32px; font-weight: 700; color: var(--blue); letter-spacing: 1px; }
  .rule { height: 3px; background: var(--blue); margin: 0 auto; }
  .welcome-card .section-title { margin-top: 84px; }
  .welcome-card .rule { width: 500px; margin-top: 14px; }
  .welcome-card p { font-size: 22px; line-height: 39px; margin: 26px 36px 0; letter-spacing: .3px; }

  .mission { position: absolute; top: 1040px; left: 0; width: 1200px; text-align: center; }
  .mission .rule { width: 504px; margin-top: 14px; }
  .mission p { width: 630px; margin: 28px auto 0; font-size: 22px; line-height: 39px; letter-spacing: .6px; }

  .what-we-do { position: absolute; top: 1433px; left: 0; width: 1200px; height: 681px; text-align: center; color: var(--white);
    background: linear-gradient(135deg, #1e2c47 0%, #15223a 45%, #2a3a58 75%, #1a2740 100%); }
  .what-we-do .section-title { color: var(--white); margin-top: 96px; }
  .what-we-do .rule { width: 500px; background: var(--white); margin-top: 12px; }
  .what-we-do ul { list-style: none; margin-top: 14px; font-size: 23px; line-height: 38.5px; letter-spacing: .5px; }

  .services { position: absolute; top: 2114px; left: 0; width: 1200px; height: 577px; background: var(--grey-bg); }
  .service-card { position: absolute; top: 82px; height: 427px; background: var(--white); text-align: center; }
  .service-icon { display: block; width: 140px; height: 110px; margin: 38px auto 0; border-radius: 10px; }
  .service-card h3 { font-size: 19px; font-weight: 700; line-height: 23px; margin-top: 32px; letter-spacing: .4px; }
  .service-card p { font-size: 16px; line-height: 29px; margin: 14px 22px 0; }
  .svc-pm { left: 28px; width: 346px; }
  .svc-pm h3 { color: var(--blue-deep); }
  .svc-pm .service-icon { background: linear-gradient(135deg, #0f66b8, #33a6d7); }
  .svc-dev { left: 405px; width: 352px; }
  .svc-dev h3 { color: var(--orange); }
  .svc-con { left: 797px; width: 362px; }
  .svc-con h3 { color: var(--teal); }
  .svc-con .service-icon { background: linear-gradient(135deg, #33b8a4, #86cfc6); }

  .site-footer { position: absolute; top: 2691px; left: 0; width: 1200px; height: 268px; background: var(--white); }
  .footer-brand { position: absolute; left: 56px; top: 96px; display: flex; align-items: center; gap: 8px; font-size: 26px; font-weight: 600; color: var(--lime); }
  .footer-brand .dot { width: 14px; height: 14px; border-radius: 50%; background: var(--lime); }
  .footer-col { position: absolute; top: 52px; }
  .footer-col h4 { font-size: 22px; font-weight: 700; color: var(--blue-deep); letter-spacing: .3px; }
  .footer-col ul { list-style: none; margin-top: 6px; font-size: 18.5px; line-height: 30.5px; color: var(--teal); }
  .col-links { left: 229px; }
  .col-company { left: 423px; }
  .col-follow { left: 956px; }
  .col-follow h4 { font-size: 19px; }

  .bottom-bar { position: absolute; top: 2959px; left: 0; width: 1200px; height: 61px; background: var(--teal); color: var(--white); font-size: 18px; display: flex; align-items: center; justify-content: space-between; padding: 0 22px; }
</style>
</head>
<body>
  <header class="site-header">
    <div class="lang-switch"><span class="flag" role="img" aria-label="Flag for English"></span>English ▾</div>
    <div class="brand-name">veltor</div>
    <nav class="main-nav">
      <a class="active" style="left:0">Home</a>
      <a style="left:139px">Services</a>
      <a style="left:306px">Mission</a>
      <a style="left:445px">Contact</a>
    </nav>
  </header>

  <div class="hero" role="img" aria-label="Photo of a modern meeting room with laptop and leather chairs"></div>

  <section class="welcome-card">
    <h1 class="section-title">WELCOME TO VELTOR</h1>
    <div class="rule"></div>
    <p>Make organization’s communication smooth and healthy with transparency and efficiency for works and tasks in all levels with our workflow tool.</p>
  </section>

  <section class="mission">
    <h2 class="section-title">OUR MISSION</h2>
    <div class="rule"></div>
    <p>Our mission is to achieve business goals with custom&shy;ers. We work together to identify the goals for your company, guides your strategy and bring the technolo&shy;gy answers which best fit to achieve the goals.</p>
  </section>

  <section class="what-we-do" role="img" aria-label="Dark blue backdrop with business charts">
    <h2 class="section-title">WHAT WE DO</h2>
    <div class="rule"></div>
    <ul>
      <li>We have a workflow tool "veltor"</li>
      <li>- Very simple end-user configurable workflow for any company processes</li>
      <li>(Targeting small-med size company)</li>
      <li>- Graphical &amp; fun features for startup users</li>
      <li>- Simple and easy task control with mailbox e-mail look &amp; feel</li>
      <li>- Non charged skill up guidance</li>
      <li>- Additional features with;</li>
      <li>Multiple delegation</li>
      <li>Clear status for each owner</li>
      <li>Task owner management console with due date reminders&amp;reporting</li>
    </ul>
  </section>

  <section class="services">
    <article class="service-card svc-pm">
      <div class="service-icon" role="img" aria-label="Illustration of a project manager beside a process chart"></div>
      <h3>Project Management<br>(PM) Service</h3>
      <p>We will provide end-to-end PM service with experienced PM. Our service is not only “managing” but “leading” to bring success to achieve the goal.</p>
    </article>
    <article class="service-card svc-dev">
      <svg class="service-icon" viewBox="0 0 140 110" role="img" aria-label="Monitor with code brackets icon">
        <rect x="12" y="4" width="116" height="80" rx="6" fill="none" stroke="#faa54b" stroke-width="7"/>
        <path d="M55 28 L40 44 L55 60 M85 28 L100 44 L85 60 M76 24 L64 64" fill="none" stroke="#faa54b" stroke-width="6" stroke-linecap="round" stroke-linejoin="round"/>
        <path d="M60 84 L56 100 M80 84 L84 100 M44 102 H96" stroke="#faa54b" stroke-width="7" stroke-linecap="round"/>
      </svg>
      <h3>System Development &amp;<br>Implementation Service</h3>
      <p>Our client list includes a wide variety of small tomedium to major sized enterprises.We can offer from full-scratch based development to packaged system implementation.</p>
    </article>
    <article class="service-card svc-con">
      <div class="service-icon" role="img" aria-label="Illustration of two people in a consultation at a table"></div>
      <h3>Consultation Service</h3>
      <p>Consulting services to a wide range of fields such as creating business strategy, business process Kaizen, IT system consultation and change management.</p>
    </article>
  </section>

  <footer class="site-footer">
    <div class="footer-brand"><span class="dot"></span>Korvan</div>
    <div class="footer-col col-links">
      <h4>QUICK LINKS</h4>
      <ul><li>Home</li><li>About Us</li><li>Services</li><li>News</li></ul>
    </div>
    <div class="footer-col col-company">
      <h4>COMPANY DETAILS</h4>
      <ul>
        <li>Name: Korvan e.U. (Registered Company)</li>
        <li>Location: A – 8010 Haldenau Mühlgasse 7</li>
        <li>C.E.O.: Ing. Lukas Demmer</li>
        <li>Establishment: 2013</li>
        <li>Industry: IT Consulting and System development</li>
      </ul>
    </div>
    <div class="footer-col col-follow">
      <h4>FOLLOW US</h4>
      <ul><li>Friendlane</li><li>Chirpwave</li><li>Workpath</li><li>Snapgrid</li></ul>
    </div>
  </footer>

  <div class="bottom-bar">
    <span>Copyright © 2018 Korvan e.U. All rights reserved</span>
    <span>Terms Of Service &nbsp;|&nbsp; Privacy Policy</span>
  </div>
</body>
</html>
```